Tallowin Climate Services WA Truck

I want a truck desing that screams Professional, Friendly and serious about work. you can find some of our work on our website, facebook and instagram.
https://breezelineclimate.com.au/
https://www.instagram.com/bzlnhvac/
https://www.facebook.com/profile.php?id=73829106548213

The design needs to include our refrigeration license: AU47325 and electrical License: EC58913
I want the colours to be consistent with my Logo.

Key Notes to be included in the design, I want to let people know we do the following;
- Commercial and Residential
- Repairs, Service and Installation
- Reverse cycle ducted Air Conditioning
- Wall Split Air Conditioning
- Ceiling Cassettes
- Evaporative Air Conditioning
- Cool Rooms
- Display Fridges
- Beer Chillers

```html
<!DOCTYPE html>
<html lang="en">
<head>
<meta charset="utf-8">
<title>Tallowin Climate Services WA – Truck Wrap</title>
<link href="https://fonts.googleapis.com/css2?family=Roboto:wght@500;700;900&display=swap" rel="stylesheet">
<style>
  :root{
    --orange:#f47a20;
    --orange-light:#f9a533;
    --orange-deep:#ec5b1c;
    --blue:#1f5fa6;
    --blue-dark:#173d78;
    --ink:#1c1c1c;
    --white:#ffffff;
    --page:#e9edf1;
  }
  *{box-sizing:border-box;margin:0;padding:0}
  html,body{width:703px;height:1200px;overflow:hidden;background:var(--page);font-family:"Roboto",Arial,sans-serif}
  .sheet{position:relative;width:703px;height:1200px}
  .panel{position:absolute;overflow:hidden;background:var(--white);box-shadow:0 2px 6px rgba(0,0,0,.18)}
  .panel svg.wrap-art{position:absolute;inset:0;width:100%;height:100%}
  .side-left{left:20px;top:20px;width:663px;height:320px}
  .side-right{left:20px;top:356px;width:663px;height:320px}
  .back-a{left:20px;top:694px;width:321px;height:486px}
  .back-b{left:362px;top:694px;width:321px;height:486px}

  .services{position:absolute;list-style:none;color:var(--ink);font-weight:500;font-size:12.5px;line-height:18.5px}
  .services li{white-space:nowrap}
  .services .dot{display:inline-block;width:7px;height:7px;border-radius:50%;background:var(--orange);margin:0 5px;vertical-align:1px}
  .services .indent{padding-left:17px}
  .services.align-right{text-align:right}
  .services.align-right .indent{padding-left:0;padding-right:17px}
  .services.small{font-size:7.5px;line-height:12px}
  .services.small .dot{width:4px;height:4px;margin:0 3px}
  .services.small .indent{padding-left:10px}
  .services.on-orange{color:var(--white)}
  .services.on-orange .dot{background:var(--white)}

  .brand{position:absolute;text-align:center;color:var(--orange);font-weight:900;text-transform:uppercase;line-height:1.05;letter-spacing:.5px}
  .brand .mark{display:inline-block;border-radius:50%;background:var(--blue);margin-bottom:6px}

  .licence-band{position:absolute;color:var(--white);font-weight:700;font-size:14px;display:flex;align-items:center;padding:0 20px}
  .email{position:absolute;color:var(--white);font-weight:500;font-size:13px}
  .phone{position:absolute;color:var(--white);font-weight:700;display:flex;align-items:center;gap:8px;white-space:nowrap}
  .web{position:absolute;color:var(--blue);font-weight:500;display:flex;align-items:center;gap:8px;white-space:nowrap}
  .icon{flex:none}
  .back-web{position:absolute;left:0;right:0;text-align:center;color:var(--white);font-weight:500;font-size:15px}
  .back-lic{position:absolute;color:var(--white);font-weight:700;font-size:10px}
</style>
</head>
<body>
<main class="sheet">

  <section class="panel side-left" aria-label="Truck body side panel, cab on right">
    <svg class="wrap-art" viewBox="0 0 663 320" preserveAspectRatio="none" aria-hidden="true">
      <defs>
        <linearGradient id="orangeFade" x1="0" y1="0" x2="1" y2="1">
          <stop offset="0" stop-color="#f9a533"/><stop offset=".6" stop-color="#f47a20"/><stop offset="1" stop-color="#ec5b1c"/>
        </linearGradient>
        <linearGradient id="bandFade" x1="0" x2="1">
          <stop offset="0" stop-color="#1f5fa6"/><stop offset=".8" stop-color="#1f5fa6"/><stop offset="1" stop-color="#1f5fa6" stop-opacity="0"/>
        </linearGradient>
      </defs>
      <path d="M0,88 C170,160 300,260 420,262 C530,262 610,210 663,160 V320 H0 Z" fill="url(#orangeFade)"/>
      <path d="M300,240 C360,275 460,272 520,250 C580,228 630,190 663,160 C600,235 500,262 420,262 C370,262 330,252 300,240 Z" fill="#fff" opacity=".9"/>
      <path d="M0,78 C170,150 300,250 420,252 C540,254 620,200 663,150" fill="none" stroke="#1f5fa6" stroke-width="5"/>
      <rect x="0" y="196" width="300" height="28" fill="url(#bandFade)"/>
    </svg>

    <ul class="services align-right" style="left:20px;top:12px;width:270px">
      <li>Commercial and Residential<span class="dot"></span></li>
      <li>Repairs, Service and Installation<span class="dot"></span></li>
      <li>Reverse cycle ducted<span class="dot"></span></li>
      <li class="indent">Air Conditioning</li>
      <li>Wall Split Air Conditioning<span class="dot"></span></li>
    </ul>
    <ul class="services align-right" style="left:380px;top:12px;width:270px">
      <li>Ceiling Cassettes<span class="dot"></span></li>
      <li>Evaporative Air Conditioning<span class="dot"></span></li>
      <li>Cool Rooms<span class="dot"></span></li>
      <li>Display Fridges<span class="dot"></span></li>
      <li>Beer Chillers<span class="dot"></span></li>
    </ul>

    <div class="brand" style="left:270px;top:100px;width:250px;font-size:22px">
      <span class="mark" style="width:26px;height:26px"></span><br>Tallowin<br>Climate Services WA
    </div>

    <div class="licence-band" style="left:0;top:196px;height:28px">AU47325 &nbsp;|&nbsp; EC58913</div>
    <div class="email" style="left:20px;top:235px">info@tallowinclimate.com.au</div>
    <div class="phone" style="left:20px;top:268px;font-size:28px">
      <svg class="icon" width="24" height="24" viewBox="0 0 24 24" aria-hidden="true"><circle cx="12" cy="12" r="11" fill="#fff"/><path d="M8.5 6.5l2 2.5-1.3 1.5c.8 1.7 2.2 3.1 3.9 3.9l1.5-1.3 2.5 2-1.2 2c-4.4-.5-8.4-4.5-8.9-8.9z" fill="#1f5fa6"/></svg>
      0400 555 218
    </div>
    <div class="web" style="left:305px;top:272px;font-size:22px">
      <svg class="icon" width="22" height="22" viewBox="0 0 22 22" aria-hidden="true"><circle cx="11" cy="11" r="10" fill="#fff"/><g fill="none" stroke="#1f5fa6" stroke-width="1.4"><circle cx="11" cy="11" r="7"/><ellipse cx="11" cy="11" rx="3" ry="7"/><path d="M4 11h14M5 7.5h12M5 14.5h12"/></g></svg>
      tallowinclimate.com.au
    </div>
  </section>

  <section class="panel side-right" aria-label="Truck body side panel, cab on left">
    <svg class="wrap-art" viewBox="0 0 663 320" preserveAspectRatio="none" aria-hidden="true">
      <g transform="translate(663,0) scale(-1,1)">
        <path d="M0,88 C170,160 300,260 420,262 C530,262 610,210 663,160 V320 H0 Z" fill="url(#orangeFade)"/>
        <path d="M300,240 C360,275 460,272 520,250 C580,228 630,190 663,160 C600,235 500,262 420,262 C370,262 330,252 300,240 Z" fill="#fff" opacity=".9"/>
        <path d="M0,78 C170,150 300,250 420,252 C540,254 620,200 663,150" fill="none" stroke="#1f5fa6" stroke-width="5"/>
        <rect x="0" y="196" width="300" height="28" fill="url(#bandFade)"/>
      </g>
    </svg>

    <ul class="services" style="left:18px;top:12px">
      <li><span class="dot"></span>Ceiling Cassettes</li>
      <li><span class="dot"></span>Evaporative Air Conditioning</li>
      <li><span class="dot"></span>Cool Rooms</li>
      <li><span class="dot"></span>Display Fridges</li>
      <li><span class="dot"></span>Beer Chillers</li>
    </ul>
    <ul class="services" style="left:400px;top:12px">
      <li><span class="dot"></span>Commercial and Residential</li>
      <li><span class="dot"></span>Repairs, Service and Installation</li>
      <li><span class="dot"></span>Reverse cycle ducted</li>
      <li class="indent">Air Conditioning</li>
      <li><span class="dot"></span>Wall Split Air Conditioning</li>
    </ul>

    <div class="brand" style="left:160px;top:100px;width:250px;font-size:22px">
      <span class="mark" style="width:26px;height:26px"></span><br>Tallowin<br>Climate Services WA
    </div>

    <div class="licence-band" style="right:0;top:196px;height:28px;justify-content:flex-end">AU47325 &nbsp;|&nbsp; EC58913</div>
    <div class="email" style="right:20px;top:235px">info@tallowinclimate.com.au</div>
    <div class="web" style="left:18px;top:272px;font-size:22px">
      <svg class="icon" width="22" height="22" viewBox="0 0 22 22" aria-hidden="true"><circle cx="11" cy="11" r="10" fill="#fff"/><g fill="none" stroke="#1f5fa6" stroke-width="1.4"><circle cx="11" cy="11" r="7"/><ellipse cx="11" cy="11" rx="3" ry="7"/><path d="M4 11h14M5 7.5h12M5 14.5h12"/></g></svg>
      tallowinclimate.com.au
    </div>
    <div class="phone" style="right:20px;top:268px;font-size:28px">
      <svg class="icon" width="24" height="24" viewBox="0 0 24 24" aria-hidden="true"><circle cx="12" cy="12" r="11" fill="#fff"/><path d="M8.5 6.5l2 2.5-1.3 1.5c.8 1.7 2.2 3.1 3.9 3.9l1.5-1.3 2.5 2-1.2 2c-4.4-.5-8.4-4.5-8.9-8.9z" fill="#1f5fa6"/></svg>
      0400 555 218
    </div>
  </section>

  <section class="panel back-a" aria-label="Rear doors, contact layout">
    <svg class="wrap-art" viewBox="0 0 321 486" preserveAspectRatio="none" aria-hidden="true">
      <path d="M0,150 C60,280 260,280 321,150 V486 H0 Z" fill="url(#orangeFade)"/>
      <rect x="0" y="264" width="321" height="22" fill="#1f5fa6"/>
      <path d="M40,250 C120,310 200,310 281,250 C220,290 100,290 40,250Z" fill="#fff"/>
      <path d="M0,486 V456 C40,425 100,418 160,418 C220,418 280,425 321,456 V486 Z" fill="#1f5fa6"/>
    </svg>
    <div class="phone" style="left:12px;top:14px;font-size:15px;color:var(--ink)">
      <svg class="icon" width="14" height="14" viewBox="0 0 24 24" aria-hidden="true"><circle cx="12" cy="12" r="11" fill="#1f5fa6"/><path d="M8.5 6.5l2 2.5-1.3 1.5c.8 1.7 2.2 3.1 3.9 3.9l1.5-1.3 2.5 2-1.2 2c-4.4-.5-8.4-4.5-8.9-8.9z" fill="#fff"/></svg>
      0400 555 218
    </div>
    <div class="email" style="right:12px;top:18px;font-size:8px;color:var(--ink)">info@tallowinclimate.com.au</div>
    <div class="brand" style="left:20px;top:120px;width:281px;font-size:20px">
      <span class="mark" style="width:22px;height:22px"></span><br>Tallowin<br>Climate Services WA
    </div>
    <div class="back-lic" style="left:12px;top:293px">AU47325</div>
    <div class="back-lic" style="right:12px;top:293px">EC58913</div>
    <ul class="services small on-orange" style="left:4px;top:320px">
      <li><span class="dot"></span>Commercial and Residential</li>
      <li><span class="dot"></span>Repairs, Service and Installation</li>
      <li><span class="dot"></span>Reverse cycle ducted</li>
      <li class="indent">Air Conditioning</li>
      <li><span class="dot"></span>Wall Split Air Conditioning</li>
    </ul>
    <ul class="services small on-orange align-right" style="right:4px;top:320px">
      <li>Ceiling Cassettes<span class="dot"></span></li>
      <li>Evaporative Air Conditioning<span class="dot"></span></li>
      <li>Cool Rooms<span class="dot"></span></li>
      <li>Display Fridges<span class="dot"></span></li>
      <li>Beer Chillers<span class="dot"></span></li>
    </ul>
    <div class="back-web" style="top:448px">tallowinclimate.com.au</div>
  </section>

  <section class="panel back-b" aria-label="Rear doors, services layout">
    <svg class="wrap-art" viewBox="0 0 321 486" preserveAspectRatio="none" aria-hidden="true">
      <path d="M0,150 C60,280 260,280 321,150 V486 H0 Z" fill="url(#orangeFade)"/>
      <rect x="0" y="264" width="321" height="22" fill="#1f5fa6"/>
      <path d="M40,250 C120,310 200,310 281,250 C220,290 100,290 40,250Z" fill="#fff"/>
      <path d="M0,486 V456 C40,425 100,418 160,418 C220,418 280,425 321,456 V486 Z" fill="#1f5fa6"/>
    </svg>
    <ul class="services small" style="left:8px;top:10px">
      <li><span class="dot"></span>Commercial and Residential</li>
      <li><span class="dot"></span>Repairs, Service and Installation</li>
      <li><span class="dot"></span>Reverse cycle ducted</li>
      <li class="indent">Air Conditioning</li>
      <li><span class="dot"></span>Wall Split Air Conditioning</li>
    </ul>
    <ul class="services small align-right" style="right:8px;top:10px">
      <li>Ceiling Cassettes<span class="dot"></span></li>
      <li>Evaporative Air Conditioning<span class="dot"></span></li>
      <li>Cool Rooms<span class="dot"></span></li>
      <li>Display Fridges<span class="dot"></span></li>
      <li>Beer Chillers<span class="dot"></span></li>
    </ul>
    <div class="brand" style="left:20px;top:120px;width:281px;font-size:20px">
      <span class="mark" style="width:22px;height:22px"></span><br>Tallowin<br>Climate Services WA
    </div>
    <div class="phone" style="left:12px;top:320px;font-size:17px">
      <svg class="icon" width="14" height="14" viewBox="0 0 24 24" aria-hidden="true"><circle cx="12" cy="12" r="11" fill="#fff"/><path d="M8.5 6.5l2 2.5-1.3 1.5c.8 1.7 2.2 3.1 3.9 3.9l1.5-1.3 2.5 2-1.2 2c-4.4-.5-8.4-4.5-8.9-8.9z" fill="#1f5fa6"/></svg>
      0400 555 218
    </div>
    <div class="email" style="left:34px;top:343px;font-size:6.5px">info@tallowinclimate.com.au</div>
    <div class="back-lic" style="right:26px;top:322px;font-size:10.5px;line-height:14px;text-align:center">AU47325<br>EC58913</div>
    <div class="back-web" style="top:448px">tallowinclimate.com.au</div>
  </section>

</main>
</body>
</html>
```